Influencer agency website

K-Brightcast, Influencer Marketing Agency. A creative space where influencers and brands meet. We represent ideas and collaborations which bring marketing success to companies and brands.
Influencer types: Nano, Micro, Macro
Brand Types: Fashion, Beauty, Luxury Goods, Gaming, Sports, Home & Living, Travel, Lifestyle, Automotive

```html
<!DOCTYPE html>
<html lang="en">
<head>
<meta charset="utf-8">
<title>K-Brightcast – Influencer Marketing Agency</title>
<link href="https://fonts.googleapis.com/css2?family=Marcellus&family=Poppins:wght@400;500;600&display=swap" rel="stylesheet">
<style>
:root{
  --peach:#f6d6c3;
  --peach-light:#f8ebe5;
  --cream:#faf8f2;
  --ink:#161618;
  --ink-soft:#25262b;
  --gold:#fbc232;
  --text:#222;
  --muted:#8a8a8a;
  --brown:#7a4a2e;
  --white:#fff;
}
*{box-sizing:border-box;margin:0;padding:0}
html,body{width:1200px;height:3555px;overflow:hidden}
body{font-family:'Poppins',sans-serif;color:var(--text);background:var(--white);position:relative}
.serif{font-family:'Marcellus',serif;font-weight:400}
.abs{position:absolute}
a{color:inherit;text-decoration:none}

/* top strip + nav */
.topbar{top:0;left:0;width:1200px;height:30px;background:var(--peach)}
.topbar .socials{position:absolute;left:905px;top:0;width:130px;height:30px;background:var(--ink);display:flex;justify-content:space-around;align-items:center;padding:0 12px}
.topbar .socials span{width:8px;height:8px;border-radius:50%;background:var(--white)}
.nav{top:30px;left:0;width:1200px;height:67px;background:var(--ink);color:var(--white)}
.brand{position:absolute;font-family:'Poppins',sans-serif;font-weight:500;color:var(--gold);font-size:14px;letter-spacing:.5px;display:flex;align-items:center;gap:7px}
.brand i{display:block;width:10px;height:10px;border-radius:50%;background:var(--gold)}
.nav .brand{left:103px;top:24px}
.nav ul{position:absolute;left:216px;top:24px;list-style:none;display:flex;gap:31px;font-size:13px;font-weight:500}
.btn{display:flex;align-items:center;justify-content:center;border-radius:30px;font-size:10px;font-weight:600;text-transform:uppercase}
.btn-gold{background:var(--gold);color:var(--ink)}
.btn-dark{background:var(--ink);color:var(--gold)}
.nav .btn{position:absolute;left:906px;top:15px;width:126px;height:36px}

/* hero */
.hero{top:97px;left:0;width:1200px;height:572px;background:linear-gradient(90deg,#f7dccb 0%,#f5d1bd 60%,#f2c3a9 100%)}
.hero h1{position:absolute;left:100px;top:92px;font-size:53px;line-height:66px;color:var(--ink)}
.hero h1 mark{background:var(--ink);color:var(--white);padding:0 6px}
.hero p{position:absolute;left:100px;top:298px;width:430px;font-size:12px;line-height:21px;color:#6d5a50}
.hero .btn{position:absolute;left:100px;top:397px;width:147px;height:41px}
.hero-photo{position:absolute;left:620px;top:20px;width:360px;height:552px;background:linear-gradient(180deg,#f0b89a 0%,#e07050 60%,#d35a42 100%);border-radius:180px 180px 0 0}
.hero-badge{position:absolute;left:920px;top:347px;width:160px;height:160px;border-radius:50%;background:var(--gold);display:flex;flex-direction:column;justify-content:center;padding-left:40px}
.hero-badge b{font-size:30px;font-weight:600;color:var(--ink)}
.hero-badge b sup{font-size:15px}
.hero-badge span{font-size:12px;color:var(--ink)}

/* about */
.about-photo{top:721px;left:0;width:596px;height:413px;background:linear-gradient(135deg,#cfd6dc,#e5d3bd 50%,#8b8f99)}
.about-side{top:721px;left:1100px;width:100px;height:413px;background:var(--cream)}
.eyebrow{font-size:9px;font-weight:600;text-transform:uppercase;color:var(--brown)}
.about .eyebrow{position:absolute;left:652px;top:719px}
.about h2{position:absolute;left:652px;top:740px;font-size:31px;color:var(--ink)}
.lede{font-size:12px;line-height:21px;color:var(--muted)}
.about .lede{position:absolute;left:652px;top:788px;width:420px}
.feature{position:absolute;display:flex;gap:12px}
.feature .ico{flex:none;width:29px;height:29px;border-radius:50%;background:var(--gold);display:flex;align-items:center;justify-content:center}
.feature h3{font-size:15px;font-weight:600;color:var(--ink)}
.feature p{font-size:12px;line-height:18px;color:var(--muted)}
.about .btn{position:absolute;left:652px;top:1088px;width:146px;height:41px}

/* why choose */
.why{top:1190px;left:0;width:1200px;height:382px;background:var(--peach-light)}
.why .eyebrow{position:absolute;left:100px;top:42px;color:var(--ink)}
.why h2{position:absolute;left:100px;top:63px;font-size:32px;color:var(--ink)}
.why .lede{position:absolute;left:100px;top:108px;width:440px}
.why-photo{position:absolute;left:597px;top:50px;width:503px;height:282px;background:linear-gradient(135deg,#b8c1ca,#e8c9c0 45%,#8895a8)}

/* services */
.services{top:1572px;left:0;width:1200px;height:685px;background:radial-gradient(circle at 0% 70%,#eeeeee 0,#fafafa 30%,#fff 60%)}
.services .eyebrow{position:absolute;width:1200px;text-align:center;top:43px}
.services h2{position:absolute;width:1200px;text-align:center;top:60px;font-size:32px;color:var(--ink)}
.card{position:absolute;width:287px;height:228px;background:var(--white);box-shadow:0 4px 20px rgba(0,0,0,.06);padding:24px 40px}
.card.active{background:var(--peach-light)}
.card svg{display:block;height:48px}
.card h3{margin-top:20px;font-size:15px;font-weight:600;color:var(--ink)}
.card p{margin-top:6px;font-size:12px;line-height:19px;color:#555}
.card .more{margin-top:16px;font-size:11.5px;color:#555;display:flex;align-items:center;gap:8px}

/* stats band */
.band{top:2257px;left:0;width:1200px;height:163px;background:var(--ink-soft);color:var(--white)}
.band h2{position:absolute;left:99px;top:46px;font-size:22px;line-height:30px;color:#f1d7b8}
.band p{position:absolute;left:400px;top:52px;width:340px;font-size:12px;line-height:21px;color:#b3b3b3}
.band .rule{position:absolute;left:775px;top:35px;width:1px;height:96px;background:#555}
.stat{position:absolute;top:46px;text-align:center;color:#f1d7b8}
.stat b{display:block;font-family:'Marcellus',serif;font-weight:400;font-size:38px;line-height:40px}
.stat span{font-size:12px;color:#b3b3b3}

/* influencers */
.influencers{top:2420px;left:0;width:1200px;height:690px}
.influencers .eyebrow{position:absolute;width:1200px;text-align:center;top:58px;color:var(--brown)}
.influencers h2{position:absolute;width:1200px;text-align:center;top:80px;font-size:32px;line-height:42px;color:var(--ink)}
.tabs{position:absolute;left:395px;top:221px;display:flex;gap:0;font-family:'Marcellus',serif;font-size:17px;color:#444}
.tabs span{padding:7px 17px}
.tabs .on{background:var(--peach-light);border-bottom:2px solid var(--gold);margin-right:18px}
.tabs span+span{margin-right:18px}
.person{position:absolute;top:321px;width:254px;height:311px;background:var(--white);box-shadow:0 4px 16px rgba(0,0,0,.08);padding:4px}
.person .photo{height:195px}
.person .stats{height:46px;background:var(--ink);display:flex;align-items:center;gap:18px;padding-left:14px;font-family:'Marcellus',serif;font-size:9px;color:#ddd}
.person .stats span{display:flex;align-items:center;gap:6px}
.person .stats i{width:18px;height:18px;border-radius:50%;background:var(--gold)}
.person h3{margin-top:18px;text-align:center;font-family:'Marcellus',serif;font-weight:400;font-size:16px;text-transform:uppercase;color:#333}
.person small{display:block;text-align:center;font-family:'Marcellus',serif;font-size:10px;color:#444}

/* footer */
.footer{top:3110px;left:0;width:1200px;height:372px;background:var(--ink);color:var(--white)}
.footer .brand{left:100px;top:75px}
.footer .about-text{position:absolute;left:100px;top:136px;width:230px;font-size:12px;line-height:18px;color:#ddd}
.footer .divider{position:absolute;left:100px;top:200px;width:230px;height:1px;background:#333}
.col h4{font-size:13px;font-weight:600;margin-bottom:14px}
.col{position:absolute;top:66px}
.col li{list-style:none;font-size:12px;line-height:26px;color:#ddd;display:flex;align-items:center;gap:8px}
.col li svg{flex:none}
.footer .social-title{position:absolute;left:100px;top:224px;font-size:13px;font-weight:600}
.footer .social-row{position:absolute;left:100px;top:263px;display:flex;gap:12px}
.footer .social-row span{width:30px;height:30px;border-radius:50%;background:var(--gold)}
.newsletter{position:absolute;left:430px;top:210px;width:670px;height:116px;background:#1f1f22;border-radius:14px}
.newsletter h4{position:absolute;left:37px;top:24px;font-size:13px;font-weight:600}
.newsletter p{position:absolute;left:37px;top:44px;width:230px;font-size:12px;line-height:18px;color:#ddd}
.newsletter .field{position:absolute;left:345px;top:32px;width:287px;height:51px;border-radius:26px;background:var(--white);color:#666;font-size:12px;display:flex;align-items:center;padding-left:22px}
.newsletter .field i{position:absolute;right:9px;top:9px;width:34px;height:34px;border-radius:50%;background:var(--gold);display:flex;align-items:center;justify-content:center}
.copyright{top:3482px;left:0;width:1200px;height:73px;background:#000;color:#ddd;font-size:11px;padding:35px 0 0 100px}
</style>
</head>
<body>

<div class="abs topbar"><div class="socials"><span></span><span></span><span></span><span></span></div></div>

<header class="abs nav">
  <div class="brand"><i></i>K-Brightcast</div>
  <ul><li>Home</li><li>About</li><li>Influencers</li><li>Page</li><li>Testimonial</li><li>Blog</li><li>Contact</li></ul>
  <a class="btn btn-gold">Get Stated</a>
</header>

<section class="abs hero">
  <h1 class="serif">Boost business<br>with <mark>influencer</mark><br>marketing</h1>
  <p>Lorem ipsum dolor sit amet, consectetur adipiscing elit. In semper vestibulum elementum. Vestibulum ante ipsum primis in faucibus orci luctus et ultrices posuere cubilia curae;</p>
  <a class="btn btn-dark">Get Stated</a>
  <div class="hero-photo" role="img" aria-label="Smiling woman in a coral printed kurta pointing upward"></div>
  <div class="hero-badge"><b>5,420 <sup>+</sup></b><span>Popular Influencer</span></div>
</section>

<section class="about">
  <div class="abs about-photo" role="img" aria-label="Businesswoman working on a laptop in a bright office with colleagues behind"></div>
  <div class="abs about-side"></div>
  <span class="eyebrow">About</span>
  <h2 class="serif">Get To Know Us</h2>
  <p class="lede">Lorem ipsum dolor sit amet, consectetur adipiscing elit. In semper vestib ulum elementum. Vestibulum ante ipsum primis in faucibus .</p>
  <div class="feature" style="left:652px;top:860px"><span class="ico"><svg width="14" height="14" viewBox="0 0 14 14"><path d="M2 3h10v6H6l-3 3V9H2z" fill="#161618"/></svg></span><div><h3>Communication</h3><p>Lorem ipsum dolor sit amet, consectetur adipiscing elit, sed do<br>eiusmod tempor incididunt.</p></div></div>
  <div class="feature" style="left:652px;top:930px"><span class="ico"><svg width="14" height="14" viewBox="0 0 14 14"><circle cx="7" cy="6" r="4" fill="#161618"/><rect x="5" y="10" width="4" height="2" fill="#161618"/></svg></span><div><h3>Creativity and Problem-Solving</h3><p>Lorem ipsum dolor sit amet, consectetur adipiscing elit, sed do<br>eiusmod tempor incididunt.</p></div></div>
  <div class="feature" style="left:652px;top:1000px"><span class="ico"><svg width="14" height="14" viewBox="0 0 14 14"><circle cx="7" cy="7" r="6" fill="#161618"/><rect x="6.2" y="3" width="1.6" height="5" fill="#fbc232"/><rect x="6.2" y="9.3" width="1.6" height="1.6" fill="#fbc232"/></svg></span><div><h3>Attention to Detail</h3><p>Lorem ipsum dolor sit amet, consectetur adipiscing elit, sed do<br>eiusmod tempor incididunt.</p></div></div>
  <a class="btn btn-dark">Get Stated</a>
</section>

<section class="abs why">
  <span class="eyebrow">Why Choose Us</span>
  <h2 class="serif">We Make Every Content Count</h2>
  <p class="lede">Lorem ipsum dolor sit amet, consectetur adipiscing elit. In semper vestib ulum elementum. Vestibulum ante ipsum primis in faucibus .</p>
  <div class="feature" style="left:100px;top:182px"><span class="ico"><svg width="14" height="14" viewBox="0 0 14 14"><circle cx="7" cy="7" r="4" fill="#161618"/></svg></span><div><h3>Years Experience</h3><p>consectetur adipiscing elit, sed do eiusmod tempor incididunt.</p></div></div>
  <div class="feature" style="left:100px;top:233px"><span class="ico"><svg width="14" height="14" viewBox="0 0 14 14"><circle cx="7" cy="4" r="2" fill="#161618"/><circle cx="3.5" cy="10" r="2" fill="#161618"/><circle cx="10.5" cy="10" r="2" fill="#161618"/></svg></span><div><h3>Professional Team</h3><p>Morbi porta, purus id porta molestie, magna ante gravida risus.</p></div></div>
  <div class="feature" style="left:100px;top:285px"><span class="ico"><svg width="14" height="14" viewBox="0 0 14 14"><path d="M7 1l5 2v4c0 3-2 5-5 6-3-1-5-3-5-6V3z" fill="#161618"/></svg></span><div><h3>Guaranteed Profit</h3><p>Sed do eiusmod tempor incididunt purus id porta molestie.</p></div></div>
  <div class="why-photo" role="img" aria-label="Team of young professionals gathered around laptops"></div>
</section>

<section class="abs services">
  <span class="eyebrow">Why Choose Us</span>
  <h2 class="serif">We Make Every Content Count</h2>
  <article class="card active" style="left:141px;top:143px">
    <svg viewBox="0 0 48 48" width="48"><circle cx="20" cy="22" r="12" fill="none" stroke="#fbc232" stroke-width="2"/><path d="M17 17l8 5-8 5z" fill="none" stroke="#fbc232" stroke-width="2"/><path d="M15 36h10M16 40h8" stroke="#fbc232" stroke-width="2"/></svg>
    <h3>Content Ideas</h3><p>Suspendisse tincidunt, odio aliquet consequat sollicitudin.</p><div class="more">Read More <svg width="12" height="8" viewBox="0 0 12 8"><path d="M0 4h10M7 1l3 3-3 3" stroke="#333" fill="none"/></svg></div>
  </article>
  <article class="card" style="left:458px;top:143px">
    <svg viewBox="0 0 48 48" width="48"><rect x="4" y="6" width="12" height="10" fill="none" stroke="#fbc232" stroke-width="2"/><rect x="30" y="6" width="12" height="10" fill="none" stroke="#fbc232" stroke-width="2"/><rect x="30" y="26" width="12" height="10" fill="none" stroke="#fbc232" stroke-width="2"/><circle cx="22" cy="24" r="5" fill="none" stroke="#fbc232" stroke-width="2"/><path d="M4 40h18" stroke="#fbc232" stroke-width="2"/></svg>
    <h3>Social Media</h3><p>Suspendisse tincidunt, odio aliquet consequat sollicitudin.</p><div class="more">Read More <svg width="12" height="8" viewBox="0 0 12 8"><path d="M0 4h10M7 1l3 3-3 3" stroke="#333" fill="none"/></svg></div>
  </article>
  <article class="card" style="left:775px;top:143px">
    <svg viewBox="0 0 48 48" width="48"><path d="M4 42h40" stroke="#fbc232" stroke-width="2"/><rect x="8" y="30" width="6" height="12" fill="none" stroke="#fbc232" stroke-width="2"/><rect x="18" y="24" width="6" height="18" fill="none" stroke="#fbc232" stroke-width="2"/><rect x="28" y="18" width="6" height="24" fill="none" stroke="#fbc232" stroke-width="2"/><path d="M6 24l14-10 8 6 14-14" stroke="#fbc232" stroke-width="2" fill="none"/></svg>
    <h3>Marketing Ads</h3><p>Suspendisse tincidunt, odio aliquet consequat sollicitudin.</p><div class="more">Read More <svg width="12" height="8" viewBox="0 0 12 8"><path d="M0 4h10M7 1l3 3-3 3" stroke="#333" fill="none"/></svg></div>
  </article>
  <article class="card" style="left:141px;top:401px">
    <svg viewBox="0 0 48 48" width="48"><rect x="4" y="8" width="40" height="28" fill="none" stroke="#fbc232" stroke-width="2"/><path d="M12 18h24M12 24h18M12 30h12M20 36v6M28 36v6" stroke="#fbc232" stroke-width="2"/></svg>
    <h3>Promotion Ads</h3><p>Suspendisse tincidunt, odio aliquet consequat sollicitudin.</p><div class="more">Read More <svg width="12" height="8" viewBox="0 0 12 8"><path d="M0 4h10M7 1l3 3-3 3" stroke="#333" fill="none"/></svg></div>
  </article>
  <article class="card" style="left:458px;top:401px">
    <svg viewBox="0 0 48 48" width="48"><rect x="4" y="4" width="18" height="14" fill="none" stroke="#fbc232" stroke-width="2"/><circle cx="13" cy="28" r="5" fill="none" stroke="#fbc232" stroke-width="2"/><path d="M4 44c0-6 4-9 9-9s9 3 9 9" fill="none" stroke="#fbc232" stroke-width="2"/><rect x="28" y="30" width="5" height="14" fill="none" stroke="#fbc232" stroke-width="2"/><rect x="37" y="22" width="5" height="22" fill="none" stroke="#fbc232" stroke-width="2"/></svg>
    <h3>Media Analytic</h3><p>Suspendisse tincidunt, odio aliquet consequat sollicitudin.</p><div class="more">Read More <svg width="12" height="8" viewBox="0 0 12 8"><path d="M0 4h10M7 1l3 3-3 3" stroke="#333" fill="none"/></svg></div>
  </article>
  <article class="card" style="left:775px;top:401px">
    <svg viewBox="0 0 48 48" width="48"><rect x="6" y="4" width="30" height="40" fill="none" stroke="#fbc232" stroke-width="2"/><circle cx="21" cy="20" r="7" fill="none" stroke="#fbc232" stroke-width="2"/><path d="M17 32h8M36 14l8 8v22h-8" fill="none" stroke="#fbc232" stroke-width="2"/></svg>
    <h3>Product Branding</h3><p>Suspendisse tincidunt, odio aliquet consequat sollicitudin.</p><div class="more">Read More <svg width="12" height="8" viewBox="0 0 12 8"><path d="M0 4h10M7 1l3 3-3 3" stroke="#333" fill="none"/></svg></div>
  </article>
</section>

<section class="abs band">
  <h2 class="serif">We are ready to serve<br>you differently.</h2>
  <p>Lorem ipsum dolor sit amet, consectetur adipiscing elit. In semper vestib ulum elementum. Vestibulum ante ipsum primis in faucibus .</p>
  <div class="rule"></div>
  <div class="stat" style="left:815px"><b>15+</b><span>Years Experience</span></div>
  <div class="stat" style="left:980px"><b>95%</b><span>Project done</span></div>
</section>

<section class="abs influencers">
  <span class="eyebrow">Explore Influencer</span>
  <h2 class="serif">Find the Perfect&nbsp; Influencers<br>for Your Business</h2>
  <div class="tabs"><span class="on">Beauty</span><span>Technology</span><span>Food</span><span>Sport</span></div>
  <article class="person" style="left:28px">
    <div class="photo" role="img" aria-label="Portrait of a smiling man in glasses and a checked shirt" style="background:linear-gradient(135deg,#d8d2c8,#8c7e70)"></div>
    <div class="stats"><span><i></i>524K followers</span><span><i></i>321K subscribers</span></div>
    <h3>Rafael Donnet</h3><small>Food Influencer</small>
  </article>
  <article class="person" style="left:324px">
    <div class="photo" role="img" aria-label="Portrait of a woman in a dark blazer" style="background:linear-gradient(135deg,#c9d6dc,#4a5560)"></div>
    <div class="stats"><span><i></i>524K followers</span><span><i></i>321K subscribers</span></div>
    <h3>Mira Castell</h3><small>Food Influencer</small>
  </article>
  <article class="person" style="left:621px">
    <div class="photo" role="img" aria-label="Portrait of a man in a grey suit" style="background:linear-gradient(135deg,#6a7a8c,#3c4450)"></div>
    <div class="stats"><span><i></i>524K followers</span><span><i></i>321K subscribers</span></div>
    <h3>Oren Whitby</h3><small>Food Influencer</small>
  </article>
  <article class="person" style="left:917px">
    <div class="photo" role="img" aria-label="Portrait of a woman in a pink top against a blue wall" style="background:linear-gradient(135deg,#5a90b0,#c85a9a)"></div>
    <div class="stats"><span><i></i>524K followers</span><span><i></i>321K subscribers</span></div>
    <h3>Tara Linwood</h3><small>Food Influencer</small>
  </article>
</section>

<footer class="abs footer">
  <div class="brand"><i></i>K-Brightcast</div>
  <p class="about-text">Sed ut perspiciatis unde omnis iste natus feria delavirot voluptatem accusantium.</p>
  <div class="divider"></div>
  <div class="col" style="left:430px"><h4>Quick Links</h4><ul>
    <li><svg width="6" height="10" viewBox="0 0 6 10"><path d="M1 1l4 4-4 4" stroke="#fbc232" fill="none" stroke-width="1.5"/></svg>About</li>
    <li><svg width="6" height="10" viewBox="0 0 6 10"><path d="M1 1l4 4-4 4" stroke="#fbc232" fill="none" stroke-width="1.5"/></svg>Services</li>
    <li><svg width="6" height="10" viewBox="0 0 6 10"><path d="M1 1l4 4-4 4" stroke="#fbc232" fill="none" stroke-width="1.5"/></svg>Blog</li>
    <li><svg width="6" height="10" viewBox="0 0 6 10"><path d="M1 1l4 4-4 4" stroke="#fbc232" fill="none" stroke-width="1.5"/></svg>Contact</li></ul></div>
  <div class="col" style="left:664px"><h4>Support Links</h4><ul>
    <li><svg width="6" height="10" viewBox="0 0 6 10"><path d="M1 1l4 4-4 4" stroke="#fbc232" fill="none" stroke-width="1.5"/></svg>Privacy Policy</li>
    <li><svg width="6" height="10" viewBox="0 0 6 10"><path d="M1 1l4 4-4 4" stroke="#fbc232" fill="none" stroke-width="1.5"/></svg>Terms &amp; Conditions</li>
    <li><svg width="6" height="10" viewBox="0 0 6 10"><path d="M1 1l4 4-4 4" stroke="#fbc232" fill="none" stroke-width="1.5"/></svg>Support</li>
    <li><svg width="6" height="10" viewBox="0 0 6 10"><path d="M1 1l4 4-4 4" stroke="#fbc232" fill="none" stroke-width="1.5"/></svg>Disclaimer</li></ul></div>
  <div class="col" style="left:906px"><h4>Support Links</h4><ul>
    <li><svg width="10" height="12" viewBox="0 0 10 12"><path d="M5 12S1 7 1 4.5a4 4 0 018 0C9 7 5 12 5 12z" fill="#fbc232"/><circle cx="5" cy="4.5" r="1.5" fill="#161618"/></svg>2187 Larkfield Ave, CA 90210, USA</li>
    <li><svg width="11" height="9" viewBox="0 0 11 9"><rect width="11" height="9" fill="#fbc232"/><path d="M0 0l5.5 5L11 0" stroke="#161618" fill="none"/></svg>hello@brightcast.example</li>
    <li><svg width="11" height="11" viewBox="0 0 11 11"><path d="M2 0l2 3-1 1.5c.8 1.5 2 2.7 3.5 3.5L8 7l3 2-1.5 2C4.5 11 0 6.5 0 1.5z" fill="#fbc232"/></svg>(+01) 555 014 2290</li></ul></div>
  <span class="social-title">Social Media</span>
  <div class="social-row"><span></span><span></span><span></span><span></span></div>
  <div class="newsletter">
    <h4>Subscribe Newsletter</h4>
    <p>Sed ut perspiciatis unde omnis iste natus feria delavirot voluptatem accusantium.</p>
    <div class="field">Enter Your Email Address<i><svg width="16" height="14" viewBox="0 0 16 14"><path d="M0 0l16 7-16 7 3-7z" fill="#161618"/></svg></i></div>
  </div>
</footer>
<div class="abs copyright">Copyright by K-Brightcast. All rights reserved.</div>

</body>
</html>
```